Website To Serve As A Resource For Medical Conditions

I need a website that is attractive that will be utilized to educate patients on either hepatitis c or HIV so it should be easily readable attractive but also professional. This website is going to be furnished with various topics for example, HIV treatment, HIV and Nutrition, HIV and Exercise, HIV and....

This website will also be cloned and utilized similarly for Hepatitis.

Coded - Design and coding required

1 page

0094D4
00A9DD
6FCCEA
C7EBF8
E9F6FB
A7469A
B969AE
D3A5CF
EDDBEB
F8F0F9
6B429C
8869AF
B7A5CE
E3DAEB
F3F0F8

```html
<!DOCTYPE html>
<html lang="en">
<head>
<meta charset="utf-8">
<title>PositivePath – HIV Education Resource</title>
<link rel="stylesheet" href="https://fonts.googleapis.com/css2?family=Open+Sans:wght@400;600;700;800&display=swap">
<style>
:root{
  --blue:#0094D4;
  --cyan:#00A9DD;
  --sky:#6FCCEA;
  --ice:#C7EBF8;
  --mist:#E9F6FB;
  --navy:#0E2050;
  --navy-deep:#0B1A3A;
  --ink:#1B2A4A;
  --text:#5B6478;
  --grey:#F2F3F5;
  --white:#ffffff;
  --line:#DDE2EA;
}
*{box-sizing:border-box;margin:0;padding:0}
html,body{width:1200px;height:5040px;overflow:hidden}
body{font-family:"Open Sans",Arial,sans-serif;color:var(--text);background:var(--white);position:relative}
.abs{position:absolute}
.eyebrow{font-size:11px;font-weight:700;letter-spacing:1px;color:var(--blue);text-transform:uppercase}
.h2{font-size:44px;font-weight:800;color:var(--navy);line-height:1.15}
.btn{display:inline-flex;align-items:center;justify-content:center;font-size:12px;font-weight:700;color:var(--white);background:var(--cyan);border-radius:3px;letter-spacing:.5px}
.photo{background:linear-gradient(135deg,#8FA7BF,#3E5874 60%,#27374F)}

/* top bar */
.topbar{top:0;left:0;width:1200px;height:60px;background:var(--white);z-index:3}
.brand{font-size:28px;font-weight:700;color:var(--blue);letter-spacing:-.5px}
.info{display:flex;align-items:center;gap:10px}
.info small{display:block;font-size:10px;font-weight:700;color:var(--ink);letter-spacing:.5px}
.info span{font-size:11px;color:var(--text)}
.quote-btn{top:12px;left:948px;width:160px;height:44px;background:var(--navy);color:var(--white);font-size:11px;font-weight:700;display:flex;align-items:center;justify-content:center;border-radius:3px}

/* hero */
.hero{top:0;left:0;width:1200px;height:860px}
.hero-overlay{inset:0;background:linear-gradient(180deg,rgba(14,32,80,.35),rgba(14,32,80,.55))}
.nav{top:68px;left:96px;width:1008px;height:56px;background:var(--white);display:flex;align-items:center;padding:0 28px;border-radius:2px;z-index:2}
.nav a{font-size:14px;font-weight:600;color:var(--ink);margin-right:38px;text-decoration:none}
.social{display:flex;gap:8px;margin-left:auto}
.social i{display:block;width:26px;height:26px;border-radius:3px}
.hero-tag{top:334px;left:0;width:1200px;text-align:center}
.hero-tag span{background:var(--cyan);color:var(--white);font-size:11px;font-weight:700;padding:6px 10px;border-radius:2px}
.hero-title{top:374px;left:0;width:1200px;text-align:center;font-size:58px;font-weight:700;color:var(--white);line-height:1.2}
.hero-btn{top:544px;left:508px;width:184px;height:46px;border:1px solid rgba(255,255,255,.8);color:var(--white);font-size:12px;font-weight:700;display:flex;align-items:center;justify-content:center;letter-spacing:.5px}
.arrow{width:46px;height:46px;background:var(--white);display:flex;align-items:center;justify-content:center;border-radius:3px}

/* about */
.about-ring{top:996px;left:96px;width:450px;height:450px;border-radius:50%;border:6px solid var(--navy)}
.about-photo{top:1008px;left:108px;width:426px;height:426px;border-radius:50%}
.about-text{top:1012px;left:612px;width:488px}
.about-text .h2{font-size:44px;margin:12px 0 18px}
.about-text p{font-size:14px;line-height:1.6;margin-bottom:18px}

/* services */
.services{top:1540px;left:0;width:1200px;height:840px;background:var(--grey)}
.card{width:320px;height:312px;border-radius:6px;overflow:hidden}
.card .shade{inset:0;background:linear-gradient(180deg,rgba(14,32,80,.15),rgba(14,32,80,.8))}
.card .icon{top:40px;left:30px;width:56px;height:56px;border:2px solid var(--white);border-radius:4px;display:flex;align-items:center;justify-content:center}
.card h3{position:absolute;top:160px;left:30px;font-size:22px;font-weight:700;color:var(--white)}
.card p{position:absolute;top:196px;left:30px;width:260px;font-size:13px;color:#E4E9F2;line-height:1.5}
.card b{position:absolute;top:248px;left:30px;font-size:14px;color:var(--white)}

/* cta band */
.cta{top:2252px;left:92px;width:1016px;height:208px;background:var(--blue);border-radius:4px;display:flex;align-items:center;padding:0 60px}
.cta h3{font-size:22px;font-weight:700;color:var(--white);flex:1}
.cta .ghost{width:160px;height:52px;border:1px solid rgba(255,255,255,.8);color:var(--white);font-size:13px;font-weight:600;display:flex;align-items:center;justify-content:center;margin-right:12px;border-radius:3px}
.cta .phone{width:210px;height:52px;background:var(--white);color:var(--navy);font-size:14px;font-weight:700;display:flex;align-items:center;justify-content:center;gap:8px;border-radius:3px}

/* why */
.feature{width:300px}
.feature h4{font-size:18px;font-weight:700;color:var(--navy);margin-bottom:6px}
.feature p{font-size:13px;line-height:1.5}
.left{text-align:right}
.dot{width:48px;height:48px;border-radius:50%;background:var(--white);border:1px solid var(--line);display:flex;align-items:center;justify-content:center}

/* reviews */
.reviews{top:3140px;left:0;width:1200px;height:520px;background:var(--grey)}
.review-side{top:3140px;left:0;width:336px;height:520px;background:var(--blue)}
.review{width:348px;height:208px;background:var(--white);border-radius:8px;padding:26px 28px;box-shadow:0 6px 20px rgba(14,32,80,.08)}
.review p{font-size:13px;line-height:1.6}
.review .who{position:absolute;left:28px;bottom:26px;display:flex;align-items:center;gap:12px;font-size:13px;font-weight:700;color:var(--ink)}
.review .who i{display:block;width:40px;height:40px;border-radius:50%;background:linear-gradient(135deg,#B9C7D8,#6C819C)}
.review .q{position:absolute;right:28px;bottom:28px;font-size:36px;font-weight:800;color:var(--navy);line-height:.6}

/* contact */
.form-box{top:3920px;left:520px;width:588px;height:408px;background:var(--white);box-shadow:0 10px 30px rgba(14,32,80,.12);padding:40px 52px}
.form-box h3{font-size:24px;font-weight:700;color:var(--navy);margin-bottom:10px}
.form-box p{font-size:13px;line-height:1.6;margin-bottom:22px}
.field{height:46px;border:1px solid var(--line);font-size:12px;color:#9AA2B1;display:flex;align-items:center;padding:0 16px;border-radius:2px}

/* footer */
.contact-strip{top:4448px;left:0;width:1200px;height:152px;background:var(--mist)}
.contact-card{top:4468px;left:92px;width:1016px;height:132px;background:var(--white);display:flex}
.contact-card div{flex:1;display:flex;flex-direction:column;align-items:center;justify-content:center;gap:12px;font-size:15px;font-weight:700;color:var(--navy)}
.footer{top:4600px;left:0;width:1200px;height:392px;background:var(--navy-deep)}
.footer h5{font-size:18px;font-weight:700;color:var(--white);margin-bottom:22px}
.footer p,.footer a{font-size:13px;line-height:1.8;color:#B6BFD1;text-decoration:none;display:block}
.bottombar{top:4992px;left:0;width:1200px;height:48px;background:var(--mist);display:flex;align-items:center;padding:0 92px;font-size:13px;font-weight:700;color:var(--navy)}
</style>
</head>
<body>

<!-- HERO -->
<section class="abs hero">
  <div class="abs photo" style="inset:0" role="img" aria-label="Doctors walking through a hospital corridor"></div>
  <div class="abs hero-overlay"></div>
  <div class="abs hero-tag"><span>WELCOME TO PositivePath</span></div>
  <h1 class="abs hero-title">Knowledge Is Our Best<br>Weapon Against HIV</h1>
  <div class="abs hero-btn">ABOUT COMPANY</div>
  <div class="abs arrow" style="top:490px;left:44px"><svg width="14" height="14" viewBox="0 0 14 14"><path d="M9 2 4 7l5 5" fill="none" stroke="#0E2050" stroke-width="2"/></svg></div>
  <div class="abs arrow" style="top:490px;left:1110px"><svg width="14" height="14" viewBox="0 0 14 14"><path d="m5 2 5 5-5 5" fill="none" stroke="#0E2050" stroke-width="2"/></svg></div>
</section>

<!-- TOP BAR -->
<header class="abs topbar">
  <div class="abs brand" style="top:14px;left:92px">PositivePath</div>
  <div class="abs info" style="top:12px;left:436px">
    <svg width="20" height="26" viewBox="0 0 20 26"><path d="M10 1a8 8 0 0 0-8 8c0 6 8 16 8 16s8-10 8-16a8 8 0 0 0-8-8z" fill="#00A9DD"/><circle cx="10" cy="9" r="3" fill="#fff"/></svg>
    <div><small>LOCATION</small><span>12 Elm Street, 4</span></div>
  </div>
  <div class="abs info" style="top:12px;left:684px">
    <svg width="22" height="22" viewBox="0 0 22 22"><circle cx="11" cy="11" r="10" fill="#00A9DD"/><path d="M11 5v6l4 3" fill="none" stroke="#fff" stroke-width="2"/></svg>
    <div><small>OFFICE HOURS</small><span>9:00 to 7:00 (Sun closed)</span></div>
  </div>
  <div class="abs quote-btn">REQUEST A QUOTE</div>
</header>

<nav class="abs nav">
  <a>Home</a><a>About Us</a><a>Services</a><a>Resources</a><a>Contact Us</a>
  <div class="social"><i style="background:#2F5DA8"></i><i style="background:#D8343B"></i><i style="background:#28A6E4"></i></div>
</nav>

<!-- ABOUT -->
<div class="abs about-ring"></div>
<div class="abs photo about-photo" role="img" aria-label="Medical team gathered around a patient, seen from above"></div>
<section class="abs about-text">
  <div class="eyebrow">About Us</div>
  <h2 class="h2">Break the Silence,<br>Break the Stigma</h2>
  <p>Clear and caring information helps people living with HIV make confident choices about their health, treatment and daily life with support from trusted care teams.</p>
  <p>We share simple guides on care, testing and wellbeing so every visitor can learn at their own pace, ask better questions and feel less alone along the way.</p>
  <div class="btn" style="width:112px;height:40px;margin-top:6px">Apply Now</div>
</section>

<!-- SERVICES -->
<section class="abs services">
  <div class="abs eyebrow" style="top:80px;left:92px">Services</div>
  <h2 class="abs h2" style="top:104px;left:92px">Information We Provide</h2>
  <div class="abs arrow" style="top:92px;left:1000px;width:44px;height:44px;box-shadow:0 2px 8px rgba(0,0,0,.08)"><svg width="12" height="12" viewBox="0 0 14 14"><path d="M9 2 4 7l5 5" fill="none" stroke="#0E2050" stroke-width="2"/></svg></div>
  <div class="abs arrow" style="top:92px;left:1056px;width:44px;height:44px;box-shadow:0 2px 8px rgba(0,0,0,.08)"><svg width="12" height="12" viewBox="0 0 14 14"><path d="m5 2 5 5-5 5" fill="none" stroke="#0E2050" stroke-width="2"/></svg></div>

  <article class="abs card" style="top:216px;left:92px">
    <div class="abs photo" style="inset:0" role="img" aria-label="Doctor discussing treatment with a patient"></div>
    <div class="abs shade"></div>
    <div class="abs icon"><svg width="26" height="26" viewBox="0 0 24 24"><path d="m12 3 2.6 5.5 6 .7-4.4 4.1 1.2 6L12 16.4 6.6 19.3l1.2-6L3.4 9.2l6-.7z" fill="none" stroke="#fff" stroke-width="1.6"/></svg></div>
    <h3>HIV treatment</h3><p>Learn how modern therapy works and why it matters.</p><b>Read More</b>
  </article>
  <article class="abs card" style="top:216px;left:440px">
    <div class="abs photo" style="inset:0" role="img" aria-label="Care team meeting around a table"></div>
    <div class="abs shade"></div>
    <div class="abs icon"><svg width="28" height="26" viewBox="0 0 28 24"><circle cx="9" cy="8" r="4" fill="none" stroke="#fff" stroke-width="1.6"/><circle cx="19" cy="8" r="4" fill="none" stroke="#fff" stroke-width="1.6"/><path d="M2 21c0-4 3-7 7-7s7 3 7 7M12 21c0-4 3-7 7-7s7 3 7 7" fill="none" stroke="#fff" stroke-width="1.6"/></svg></div>
    <h3>HIV and Nutrition</h3><p>Simple eating habits that support a strong body.</p><b>Read More</b>
  </article>
  <article class="abs card" style="top:216px;left:788px">
    <div class="abs photo" style="inset:0" role="img" aria-label="Smiling doctor in a clinic"></div>
    <div class="abs shade"></div>
    <div class="abs icon"><svg width="26" height="26" viewBox="0 0 24 24"><circle cx="14" cy="4" r="2.4" fill="none" stroke="#fff" stroke-width="1.6"/><path d="M7 21l4-7 3 3v4M11 14l1-5 4 3h3M12 9 8 10l-2 3" fill="none" stroke="#fff" stroke-width="1.6"/></svg></div>
    <h3>HIV and Exercise</h3><p>Safe ways to stay active and build your energy.</p><b>Read More</b>
  </article>

  <div class="abs btn" style="top:604px;left:512px;width:176px;height:40px">Contact Us</div>
</section>

<!-- CTA -->
<section class="abs cta">
  <h3>Delivering Results with Solid Dependability</h3>
  <div class="ghost">Get in Touch</div>
  <div class="phone"><svg width="14" height="14" viewBox="0 0 24 24"><path d="M6 2h4l2 5-3 2a11 11 0 0 0 6 6l2-3 5 2v4a2 2 0 0 1-2 2A18 18 0 0 1 4 4a2 2 0 0 1 2-2z" fill="#0094D4"/></svg>+000 555 - 01234</div>
</section>

<!-- WHY CHOOSE US -->
<section>
  <div class="abs eyebrow" style="top:2520px;left:0;width:1200px;text-align:center">Why Choose Us</div>
  <h2 class="abs h2" style="top:2540px;left:0;width:1200px;text-align:center">Why Choose Us</h2>
  <svg class="abs" style="top:2620px;left:400px" width="400" height="400" viewBox="0 0 400 400"><circle cx="200" cy="200" r="190" fill="none" stroke="#DDE2EA" stroke-width="1.5" stroke-dasharray="4 6"/></svg>
  <div class="abs photo" style="top:2580px;left:440px;width:320px;height:320px;border-radius:50%" role="img" aria-label="Portrait of a doctor in a white coat holding a stethoscope"></div>

  <div class="abs dot" style="top:2668px;left:364px"><svg width="22" height="22" viewBox="0 0 24 24"><path d="M12 20S3 14 3 8.5A4.5 4.5 0 0 1 12 6a4.5 4.5 0 0 1 9 2.5C21 14 12 20 12 20z" fill="none" stroke="#0094D4" stroke-width="1.6"/></svg></div>
  <div class="abs dot" style="top:2822px;left:340px"><svg width="22" height="22" viewBox="0 0 24 24"><circle cx="12" cy="12" r="9" fill="none" stroke="#0094D4" stroke-width="1.6"/><path d="M12 7v5l3 2" fill="none" stroke="#0094D4" stroke-width="1.6"/></svg></div>
  <div class="abs dot" style="top:2976px;left:364px"><svg width="22" height="22" viewBox="0 0 24 24"><path d="M4 5h6v15H4zM14 5h6v15h-6z" fill="none" stroke="#0094D4" stroke-width="1.6"/></svg></div>
  <div class="abs dot" style="top:2668px;left:788px"><svg width="22" height="22" viewBox="0 0 24 24"><circle cx="12" cy="7" r="3.5" fill="none" stroke="#0094D4" stroke-width="1.6"/><path d="M5 21c0-4 3-7 7-7s7 3 7 7" fill="none" stroke="#0094D4" stroke-width="1.6"/></svg></div>
  <div class="abs dot" style="top:2822px;left:812px"><svg width="22" height="22" viewBox="0 0 24 24"><path d="m12 3 2.6 5.5 6 .7-4.4 4.1 1.2 6L12 16.4 6.6 19.3l1.2-6L3.4 9.2l6-.7z" fill="none" stroke="#0094D4" stroke-width="1.6"/></svg></div>
  <div class="abs dot" style="top:2976px;left:788px"><svg width="22" height="22" viewBox="0 0 24 24"><path d="M12 3 4 6v6c0 5 3.5 8 8 9 4.5-1 8-4 8-9V6z" fill="none" stroke="#0094D4" stroke-width="1.6"/></svg></div>

  <div class="abs feature left" style="top:2680px;left:40px"><h4>Empathy and Support</h4><p>Kind guidance for every<br>step of your journey.</p></div>
  <div class="abs feature left" style="top:2812px;left:20px"><h4>Regular Updates</h4><p>Fresh facts reviewed<br>by our care experts.</p></div>
  <div class="abs feature left" style="top:2944px;left:40px"><h4>Resource Library</h4><p>Guides and tools in<br>one easy place.</p></div>
  <div class="abs feature" style="top:2680px;left:860px"><h4>Non-Discrimination</h4><p>Everyone is welcome<br>and treated with respect.</p></div>
  <div class="abs feature" style="top:2812px;left:884px"><h4>Supportive Community</h4><p>Connect with people<br>who understand.</p></div>
  <div class="abs feature" style="top:2944px;left:860px"><h4>Anonymous Support</h4><p>Ask questions privately<br>without judgement.</p></div>
</section>

<!-- REVIEWS -->
<section>
  <div class="abs reviews"></div>
  <div class="abs review-side"></div>
  <div class="abs eyebrow" style="top:3228px;left:0;width:1200px;text-align:center">Testimonials</div>
  <h2 class="abs h2" style="top:3248px;left:0;width:1200px;text-align:center">Client Reviews</h2>

  <article class="abs review" style="top:3332px;left:132px">
    <p>The guides helped me understand my treatment and talk openly with my doctor. I finally feel in control of my health and my future plans.</p>
    <div class="who"><i></i>Sam Rivers</div><div class="q">”</div>
  </article>
  <article class="abs review" style="top:3332px;left:500px">
    <p>Clear, friendly and easy to read. The nutrition tips made a real difference to my energy and to how I plan meals for my family each week.</p>
    <div class="who"><i></i>Sam Rivers</div><div class="q">”</div>
  </article>
  <article class="abs review" style="top:3332px;left:868px">
    <p>I found answers here that I was too shy to ask about. The support pages gave me hope and practical steps to stay healthy and active.</p>
    <div class="who"><i></i>Sam Rivers</div><div class="q">”</div>
  </article>

  <svg class="abs" style="top:3580px;left:624px" width="80" height="16" viewBox="0 0 80 16"><circle cx="8" cy="8" r="6" fill="none" stroke="#0E2050" stroke-width="1.5"/><circle cx="8" cy="8" r="2.5" fill="#0E2050"/><circle cx="30" cy="8" r="3" fill="#AAB3C3"/><circle cx="46" cy="8" r="3" fill="#AAB3C3"/><circle cx="62" cy="8" r="3" fill="#AAB3C3"/></svg>
</section>

<!-- CONTACT FORM -->
<section>
  <div class="abs eyebrow" style="top:3784px;left:0;width:1200px;text-align:center">Our Form</div>
  <h2 class="abs h2" style="top:3808px;left:0;width:1200px;text-align:center">Get in touch with us</h2>
  <div class="abs photo" style="top:3920px;left:92px;width:428px;height:408px" role="img" aria-label="Doctor reviewing notes with a patient"></div>
  <div class="abs" style="top:4240px;left:284px;width:212px;height:60px;background:var(--white);display:flex;align-items:center;justify-content:center;gap:12px;font-size:16px;font-weight:700;color:var(--navy)">
    <svg width="20" height="20" viewBox="0 0 24 24"><path d="M6 2h4l2 5-3 2a11 11 0 0 0 6 6l2-3 5 2v4a2 2 0 0 1-2 2A18 18 0 0 1 4 4a2 2 0 0 1 2-2z" fill="#0E2050"/></svg>1800-555-0142
  </div>
  <div class="abs form-box">
    <h3>Get Free Consultation</h3>
    <p>Get a free consultation from our experts. Our customer support team<br>helps you 24/7. Don't hesitate.</p>
    <div class="field" style="margin-bottom:16px">Your Name</div>
    <div style="display:flex;gap:14px;margin-bottom:16px"><div class="field" style="flex:1">Your Email</div><div class="field" style="flex:1">Message</div></div>
    <div class="btn" style="width:100%;height:50px">GET IN TOUCH &nbsp;→</div>
  </div>
</section>

<!-- FOOTER -->
<div class="abs contact-strip"></div>
<div class="abs contact-card">
  <div><svg width="30" height="30" viewBox="0 0 24 24"><path d="M12 2a7 7 0 0 0-7 7c0 5 7 13 7 13s7-8 7-13a7 7 0 0 0-7-7z" fill="none" stroke="#0094D4" stroke-width="1.6"/><circle cx="12" cy="9" r="2.5" fill="none" stroke="#0094D4" stroke-width="1.6"/></svg>Come to Our Location</div>
  <div><svg width="30" height="30" viewBox="0 0 24 24"><rect x="3" y="5" width="18" height="14" rx="1" fill="none" stroke="#0094D4" stroke-width="1.6"/><path d="m3 6 9 7 9-7" fill="none" stroke="#0094D4" stroke-width="1.6"/></svg>Send Us an Email</div>
  <div><svg width="30" height="30" viewBox="0 0 24 24"><path d="M6 2h4l2 5-3 2a11 11 0 0 0 6 6l2-3 5 2v4a2 2 0 0 1-2 2A18 18 0 0 1 4 4a2 2 0 0 1 2-2z" fill="none" stroke="#0094D4" stroke-width="1.6"/></svg>Give Us a Call</div>
</div>

<footer class="abs footer">
  <div class="abs" style="top:64px;left:92px;width:300px">
    <div class="brand" style="margin-bottom:16px">PositivePath</div>
    <p>Trusted learning for people living with HIV, their families and friends. Simple facts, real support and a caring voice whenever you need it most.</p>
  </div>
  <div class="abs" style="top:72px;left:436px;width:300px">
    <h5>Visit Our Place</h5>
    <p>88 Harbor Lane, Suite 5,<br>Northfield, USA</p>
    <p style="color:var(--white);font-weight:700;margin-top:6px">+000 555 - 01234</p>
    <div style="display:flex;margin-top:22px"><div style="width:200px;height:40px;border:1px solid #33456E;font-size:12px;color:#8A95AC;display:flex;align-items:center;padding:0 14px">Enter Your Email</div><div style="width:100px;height:40px;background:var(--blue);color:var(--white);font-size:11px;font-weight:700;display:flex;align-items:center;justify-content:center">SUBSCRIBE</div></div>
  </div>
  <div class="abs" style="top:72px;left:788px;width:320px">
    <h5>Useful Links</h5>
    <div style="display:flex;gap:60px">
      <div><a>About Us</a><a>Practice areas</a><a>Why Choose Us</a><a>How it works</a><a>News &amp; Updates</a></div>
      <div><a>Testimonials</a><a>FAQs</a><a>Cookies</a><a>Contact Us</a><a>Privacy Policy</a></div>
    </div>
  </div>
</footer>

<div class="abs bottombar">PositivePath
  <div style="margin-left:auto;display:flex;gap:10px"><i style="display:block;width:12px;height:12px;background:var(--navy);border-radius:50%"></i><i style="display:block;width:12px;height:12px;background:var(--navy);border-radius:50%"></i><i style="display:block;width:12px;height:12px;background:var(--navy);border-radius:50%"></i><i style="display:block;width:12px;height:12px;background:var(--navy);border-radius:50%"></i></div>
</div>
<div class="abs" style="top:4960px;left:1132px;width:48px;height:48px;background:var(--cyan);border-radius:4px;display:flex;align-items:center;justify-content:center"><svg width="16" height="16" viewBox="0 0 16 16"><path d="m3 10 5-5 5 5" fill="none" stroke="#fff" stroke-width="2"/></svg></div>

</body>
</html>
```